Business Card for Dental Office

Our office is in the Hillcrest section of San Diego, California which is a well-established area. Maybe the back can be a map of our office location

```html
<!DOCTYPE html>
<html lang="en">
<head>
<meta charset="UTF-8">
<title>Crestline Dental – Business Card</title>
<link rel="stylesheet" href="https://fonts.googleapis.com/css2?family=Tinos&display=swap">
<style>
  :root {
    --page-bg: #e9e7e4;
    --card-black: #050505;
    --card-white: #ffffff;
    --ink: #111111;
    --silver: #d9d9d9;
    --card-shadow: rgba(0, 0, 0, 0.18);
  }
  html, body {
    margin: 0;
    padding: 0;
    width: 1200px;
    height: 900px;
    overflow: hidden;
    background: var(--page-bg);
    font-family: "Tinos", "Times New Roman", serif;
  }
  .canvas {
    position: relative;
    width: 1200px;
    height: 900px;
  }
  .card {
    position: absolute;
    left: 320px;
    width: 560px;
    height: 320px;
    box-shadow: 0 6px 18px var(--card-shadow);
    overflow: hidden;
  }
  /* Front face */
  .card-front {
    top: 110px;
    background: var(--card-black);
    display: flex;
    align-items: center;
    justify-content: center;
  }
  .front-brand {
    display: flex;
    align-items: center;
    gap: 12px;
    color: var(--silver);
    font-size: 34px;
    letter-spacing: 0.5px;
  }
  .front-brand .brand-mark {
    width: 14px;
    height: 14px;
    border-radius: 50%;
    background: var(--silver);
  }
  /* Back face */
  .card-back {
    top: 470px;
    background: var(--card-white);
    color: var(--ink);
  }
  .accent-bar {
    position: absolute;
    left: 0;
    top: 118px;
    width: 22px;
    height: 170px;
    background: var(--card-black);
    border-radius: 0 8px 8px 0;
  }
  .corner-brand {
    position: absolute;
    top: 14px;
    right: 16px;
    font-size: 13px;
    color: var(--ink);
  }
  .contact {
    position: absolute;
    left: 30px;
    top: 140px;
    line-height: 1.05;
  }
  .contact-name {
    margin: 0;
    font-size: 24px;
    font-weight: 400;
  }
  .contact-title {
    margin: 0 0 12px;
    font-size: 17px;
  }
  .contact-details {
    margin: 0;
    font-size: 16px;
    font-style: normal;
    line-height: 1.02;
  }
</style>
</head>
<body>
<main class="canvas">
  <section class="card card-front" aria-label="Card front">
    <div class="front-brand">
      <span class="brand-mark"></span>
      <span class="brand-name">Crestline Dental</span>
    </div>
  </section>

  <section class="card card-back" aria-label="Card back">
    <div class="accent-bar"></div>
    <div class="corner-brand">Crestline Dental</div>
    <div class="contact">
      <h1 class="contact-name">Maya Ellison</h1>
      <p class="contact-title">Chief Executive Officer</p>
      <address class="contact-details">
        Suite 12, 41 Harbor Lane<br>
        Lakeview<br>
        Phone: 555 010 247<br>
        Cell: 5550 138 62<br>
        Email: maya@crestlinedental.com
      </address>
    </div>
  </section>
</main>
</body>
</html>
```